brivox new business card design project

we need a new business card design. you can view info about us @ brivox.com. i have attached an example of our previous card with our previous name that we no longer use. We really liked the design, colors etc. look below to see more info about this project. it asks for a limited number of words. please see our website for more info about our compnay.

Target Market(s)

law enforcement

Contact Information for Business Card

i have uploaded an example of what we used before that we liked.

Font styles to use
Serif

```html
<!DOCTYPE html>
<html lang="en">
<head>
<meta charset="utf-8">
<title>Brivox Business Card</title>
<link href="https://fonts.googleapis.com/css2?family=Lato:wght@300;400;700&display=swap" rel="stylesheet">
<style>
  :root {
    --backdrop: #3b3531;
    --card: #0e1f2a;
    --card-edge: #0a161e;
    --ink: #ffffff;
    --ink-soft: #d9dfe3;
    --rule: #4d5d68;
    --mark: #c9cfd3;
  }
  * { margin: 0; padding: 0; box-sizing: border-box; }
  html, body {
    width: 1200px;
    height: 844px;
    overflow: hidden;
    background: var(--backdrop);
    font-family: "Lato", sans-serif;
  }
  .stage {
    position: relative;
    width: 1200px;
    height: 844px;
  }
  .card {
    position: absolute;
    top: 279px;
    width: 500px;
    height: 286px;
    background: var(--card);
    border: 1px solid var(--card-edge);
    box-shadow: 0 10px 24px rgba(0,0,0,0.45);
    color: var(--ink);
  }
  .card--front { left: 60px; }
  .card--back { left: 640px; }

  .wordmark {
    position: absolute;
    font-weight: 300;
    letter-spacing: 0.14em;
    color: var(--ink);
    line-height: 1;
  }
  .card--front .wordmark {
    top: 34px;
    right: 34px;
    font-size: 38px;
  }
  .rule {
    position: absolute;
    left: 34px;
    right: 34px;
    height: 1px;
    background: var(--rule);
  }
  .rule--top { top: 92px; }
  .rule--mid { top: 190px; }
  .rule--low { top: 228px; }

  .person {
    position: absolute;
    left: 34px;
    top: 118px;
  }
  .person__name {
    font-weight: 700;
    font-size: 17px;
    letter-spacing: 0.02em;
    line-height: 1.1;
  }
  .person__title {
    font-weight: 300;
    font-size: 14px;
    color: var(--ink-soft);
    line-height: 1.2;
  }
  .address {
    position: absolute;
    left: 34px;
    top: 164px;
    font-weight: 300;
    font-size: 14px;
  }
  .contact {
    position: absolute;
    left: 34px;
    top: 201px;
    font-weight: 300;
    font-size: 13.5px;
    white-space: nowrap;
  }
  .contact b { font-weight: 700; }
  .contact .sep { margin: 0 6px; color: var(--ink-soft); }
  .services {
    position: absolute;
    left: 34px;
    top: 240px;
    font-weight: 300;
    font-size: 13.5px;
    white-space: nowrap;
  }
  .services .dot {
    display: inline-block;
    width: 6px;
    height: 6px;
    border-radius: 50%;
    background: var(--ink);
    margin: 0 4px 2px 6px;
    vertical-align: middle;
  }

  .card--back .wordmark {
    top: 92px;
    left: 0;
    right: 0;
    text-align: center;
    font-size: 44px;
    color: var(--mark);
  }
  .card--back .rule {
    top: 166px;
    left: 96px;
    right: 96px;
  }
  .tagline {
    position: absolute;
    top: 180px;
    left: 0;
    right: 0;
    text-align: center;
    font-size: 11.5px;
    font-weight: 400;
    letter-spacing: 0.06em;
    color: var(--ink-soft);
  }
</style>
</head>
<body>
<main class="stage">
  <section class="card card--front" aria-label="Business card front">
    <div class="wordmark">BRIVOX</div>
    <div class="rule rule--top"></div>
    <div class="person">
      <div class="person__name">DANIEL PORTER</div>
      <div class="person__title">Managing Director</div>
    </div>
    <div class="address">4215 Meridian Lane Austin, TX 78701</div>
    <div class="rule rule--mid"></div>
    <div class="contact"><b>P:</b> 866.555.0142<span class="sep">|</span><b>E:</b> info@brivox.com<span class="sep">|</span><b>W:</b> www.brivox.com</div>
    <div class="rule rule--low"></div>
    <div class="services">Law Enforcement<span class="dot"></span>Justice of the Peace<span class="dot"></span>Municipal Courts</div>
  </section>

  <section class="card card--back" aria-label="Business card back">
    <div class="wordmark">BRIVOX</div>
    <div class="rule"></div>
    <div class="tagline">LAW ENFORCEMENT INNOVATION</div>
  </section>
</main>
</body>
</html>
```